Plumbury Product Booklet - Content/Assets Provided...Need Inspirational layout!

We require you to design a 12 page booklet to be included with our Plumbury range of products.

We have a strong idea of what will go on each page and have all content ready for you (see enclosed document). We also have most of the assets available as well - also attached.

We require each page to be brimming with information but also need them to have a feeling of being uncluttered.

We need a theme running through the booklet so each page feels that is is part of the booklet and is visually consistent with all the other pages.

Deliverable will be a high quality PDF with 12 individual A5 pages in the correct order 1-12

Technical Specification:

Format:148 x 210 mm A5

Set type and images 1.5 mm away from edge
Bleed of 2 mm has to be added

So total page size of 152 x 214 mm including bleed.

Number of pages 12

The page sequence must be continuous in the PDF document.

Front cover = 1st page
All following pages = 2nd, 3rd, 4th, 5th, 6th page, etc.

Colours inside: 4/4-coloured CMYK

Print data: Not less than 300dpi as PDF in the CMYK colour range with the "ISO Coated v2 (Fogra 39 L)" colour profile for illustration printing paper and "PSO Uncoated ISO12647 (Fogra 47L)" for offset or recycling paper. Please do not use any spot colours or special colours.

Paper will be135 gsm Coated art paper (Glossy) with a staple binding.

We have included an image of a previous front/back cover design.

Files attached include: logo's; screenshot of front/back cover idea from another designer; our 'cartoon' background image that runs through all of our Plumbury branding; assorted photographs that could be used (please feel free to use all/none or your own imagery). Lastly there is the content document (PDF) with details of the 12 pages we need.

**Any questions - fire away! Will get back to you as soon as possible.**
Updates

First of all many thanks for those who have contributed to an initial design. For those who want to submit there are three days left so feel free to post. Looking forward to feeding back soon... Added Tuesday, January 31, 2017

Target Market(s)

The booklet will be read by those who have already purchased the item so isn't a sales document. However, it is essential that the booklet provides positive reinforcement that they have purchased the correct product and it is was the best option for their baby.

Industry/Entity Type

Baby

Font styles to use
Sans Serif

Requirements
Must have
• Inspired layout!
• Tidy, uncluttered and consistent look for all 12 pages...
• Colour palette to be based on the 'background image' provided. This image runs through all the Plumbury branding we have.
• Please let us know if you require any modifications to the images/assets e.g. higher resolution or queries with content provided.
Nice to have
• Additional imagery can be provided by designer - must be relevant and enhance the design. Surprise us! :o)
Should not have
• Don't want the look of a 'cookie cutter' template.

```html
<!DOCTYPE html>
<html lang="en">
<head>
<meta charset="utf-8">
<title>Plumbury Booklet – Pages 8–9</title>
<link rel="stylesheet" href="https://fonts.googleapis.com/css2?family=Nunito:wght@700&family=Nunito+Sans:wght@400;700&display=swap">
<style>
  :root {
    --bg: #e9e6e2;
    --paper: #ffffff;
    --ink: #2b2b2b;
    --green: #8cc63f;
    --teal: #1ba6d9;
    --link: #1d96d3;
    --sky: #a9dcf3;
    --grass: #b9dc8a;
  }
  * { box-sizing: border-box; margin: 0; padding: 0; }
  html, body { width: 1200px; height: 1200px; overflow: hidden; background: var(--bg); }
  body { position: relative; font-family: "Nunito Sans", Arial, sans-serif; color: var(--ink); }

  .spread {
    position: absolute; left: 20px; top: 189px; width: 1160px; height: 822px;
    display: flex; box-shadow: 0 6px 24px rgba(0,0,0,.18);
  }
  .page { position: relative; width: 580px; height: 822px; overflow: hidden; background: var(--paper); }

  .page--left {
    background:
      radial-gradient(ellipse 70% 40% at 0% 0%, rgba(169,220,243,.95), transparent 70%),
      var(--paper);
  }
  .page--right {
    background: linear-gradient(180deg, var(--sky) 0%, #e4f4fb 35%, #ffffff 58%, #ffffff 100%);
  }

  .headline {
    position: absolute; left: 39px; top: 72px;
    font-family: "Nunito", "Nunito Sans", sans-serif;
    font-size: 33px; line-height: 34px; font-weight: 700;
  }
  .headline--green { color: var(--green); }
  .headline--teal { color: var(--teal); left: 59px; width: 350px; }

  .body-copy { position: absolute; font-size: 13.2px; line-height: 16.6px; }
  .body-copy p { margin-bottom: 8px; }
  .page--left .body-copy { left: 39px; top: 154px; width: 482px; }
  .page--right .body-copy { left: 59px; top: 186px; width: 344px; }

  .read-more { position: absolute; z-index: 2; font-weight: 700; color: var(--link); font-size: 13.5px; line-height: 18px; }
  .page--left .read-more { left: 39px; top: 500px; }
  .page--right .read-more { left: 59px; top: 700px; }

  .photo-feeding {
    position: absolute; left: 0; top: 440px; width: 580px; height: 352px;
    background: linear-gradient(160deg, #f3ede6 0%, #e9d2bf 40%, #e6b993 65%, #c9c38d 100%);
    -webkit-mask-image: linear-gradient(180deg, transparent 0%, #000 28%);
    mask-image: linear-gradient(180deg, transparent 0%, #000 28%);
  }

  .illus-kite {
    position: absolute; left: 408px; top: 96px; width: 153px; height: 132px;
    border-radius: 10px;
    background: linear-gradient(135deg, rgba(27,166,217,.35), rgba(140,198,63,.35), rgba(247,181,44,.35), rgba(233,78,60,.3));
  }
  .illus-balloon {
    position: absolute; left: 401px; top: 266px; width: 62px; height: 89px;
    border-radius: 10px;
    background: linear-gradient(180deg, rgba(246,226,210,.8), rgba(255,255,255,.6));
  }
  .illus-hills {
    position: absolute; left: 0; bottom: 0; width: 580px; height: 240px;
    background: linear-gradient(180deg, rgba(185,220,138,0) 0%, rgba(185,220,138,.5) 45%, var(--grass) 100%);
  }

  .folio { position: absolute; z-index: 2; top: 752px; font-weight: 700; font-size: 12px; color: #fff; }
  .page--left .folio { left: 39px; }
  .page--right .folio { right: 44px; }
</style>
</head>
<body>
  <main class="spread">
    <section class="page page--left">
      <h2 class="headline headline--green">How my baby’s reflux<br>affected my whole family</h2>
      <div class="body-copy">
        <p>Apart from the obvious anxiety and frustration parents feel when they can’t resolve a baby’s health issues or take them on themselves, there are some very subtle undercurrents that can impact on a family coping with a baby suffering with reflux.</p>
        <p>From my own personal experiences with our third child Maisie, I felt guilty that I couldn’t spend more time with my other children. At first with a newborn, it was expected that I was busy feeding, washing, sleeping alongside our new daughter, mirroring her random moments of sleep and my husband spent a lot of time making sure that our two other children received his attention when I was in this early routine. It seemed to be endless though and I found myself feeling more ‘split’ between my children as time moved on and Maisie didn’t improve.</p>
        <p>To me it seemed like too much to ask them to grow up fast and just deal with the fact that their little sister was ill. They were just as scared as us when Maisie would scream from tea time and into the late evening, but we had to show that we; as parents; were in control. Bedtime was tough because we’d be holding Maisie as well as trying to get our other two girls off to bed. Most of the time we weren’t in control and I definitely developed symptoms of depression during this period.</p>
      </div>
      <div class="photo-feeding" role="img" aria-label="Photo of a baby in a high chair being fed with a spoon"></div>
      <p class="read-more">See the rest of the article here:<br>www.calmtummy.org/family</p>
      <span class="folio">8</span>
    </section>

    <section class="page page--right">
      <div class="illus-hills" role="img" aria-label="Illustration of soft green rolling hills"></div>
      <div class="illus-kite" role="img" aria-label="Illustration of a rainbow-coloured kite with ribbon tails"></div>
      <div class="illus-balloon" role="img" aria-label="Illustration of a pale hot air balloon"></div>
      <h2 class="headline headline--teal">I knew my screaming baby had more than ‘just colic’</h2>
      <div class="body-copy">
        <p>As with so many first-time parents, my husband Tom and I had a starry-eyed view of how things would be once we had our much wanted baby. So when Oscar arrived, ten days earlier than expected and following a smooth birth, we left hospital within hours, eager to start the perfect family life we anticipated.</p>
        <p>That night, after five hours of attempting to breastfeed, rocking, fan off, fan on (it was summer), Moses basket, our bed, with vest, without vest, we all finally fell into a deep sleep at 4am. This was not how it was meant to be; we were in shock.</p>
        <p>Over the next four weeks, a worrying pattern developed. After each feed, Oscar would arch his body and throw his head backwards with surprising force.</p>
        <p>His crying escalated from a few tears to a scared, inconsolable screeching, sometimes to the point of choking. Well-meaning midwives, health visitors, family, friends and our GP all tried to reassure us it was ‘just colic - all babies get it’. Over-the-counter remedies which others swore by raised our hopes but did not ease the problem.</p>
        <p>When we were told it would pass by three months, we were desperate; we did not know how to get through the next three hours. Racked with self-doubt about our parenting skills, we searched the internet tirelessly and read endless books. Had I eaten something which was affecting the breast milk? Was he feeding in the wrong position? Had we winded him enough?</p>
      </div>
      <p class="read-more">See the rest of the article here:<br>www.calmtummy.org/colic</p>
      <span class="folio">9</span>
    </section>
  </main>
</body>
</html>
```